Single Page Digital Brochure

We are a Sydney based finance company. We lend money to developers. Please see attached example of what we are looking to have produced. We just need a design which can be posted on LINKEDIN

Target Market(s)

Property Developers who are borrowing money

Industry/Entity Type

Finance

Requirements
Must have
• Australian relevant imagery.

TEXT TO INCLUDE:

New Offering from Ferngate Lending
Nice to have
• Design and colour scheme based around our logo (attached)

Please include the same text as the attachment

Please make the design based loosely on the attachment. But do not copy the attachement
Should not have
• Remove Text: 'Settle in under four days'

```html
<!DOCTYPE html>
<html lang="en">
<head>
<meta charset="utf-8">
<title>Ferngate Lending – New Offering</title>
<link rel="stylesheet" href="https://fonts.googleapis.com/css2?family=Oswald:wght@500&family=Roboto:wght@400;500&family=Ubuntu:wght@500&display=swap">
<style>
  :root {
    --forest: #264c37;
    --paper: #ffffff;
    --ink: #1d1d1d;
    --backdrop: #8c8c8c;
    --sky: #e4e4e4;
    --haze: #cbcbcb;
    --city-mid: #8f8f8f;
    --city-deep: #6a6a6a;
    --city-light: #b4b4b4;
  }
  * { box-sizing: border-box; margin: 0; padding: 0; }
  html, body { width: 1200px; height: 1200px; overflow: hidden; }
  body { background: var(--backdrop); position: relative; font-family: "Roboto", sans-serif; }

  .brochure {
    position: absolute; left: 64px; top: 218px;
    width: 1072px; height: 764px;
    background: var(--paper);
  }
  .city-photo {
    position: absolute; left: 0; top: 24px; width: 730px; height: 717px;
    background: linear-gradient(180deg,
      #d6d6d6 0%, var(--sky) 14%, #dcdcdc 24%, var(--haze) 29%,
      #a9a9a9 36%, var(--city-mid) 48%, var(--city-deep) 62%,
      #858585 76%, var(--city-light) 90%, #c2c2c2 100%);
  }
  .title-block {
    position: absolute; left: 42px; top: 0; width: 350px; height: 243px;
    background: var(--forest); color: var(--paper);
    padding: 46px 0 0 26px;
  }
  .title-kicker { font-size: 21px; letter-spacing: 0.3px; line-height: 1; }
  .title-name {
    font-family: "Oswald", sans-serif; font-weight: 500;
    font-size: 67px; line-height: 70px; margin-top: 10px; text-transform: uppercase;
  }

  .brand {
    position: absolute; left: 770px; top: 84px; width: 256px;
    display: flex; align-items: center; gap: 10px; justify-content: center;
    color: var(--forest);
  }
  .brand-dot { width: 22px; height: 22px; border-radius: 50%; background: var(--forest); flex: none; }
  .brand-name { font-family: "Ubuntu", sans-serif; font-weight: 500; font-size: 24px; white-space: nowrap; }

  .headline {
    position: absolute; left: 758px; top: 196px;
    font-family: "Ubuntu", sans-serif; font-weight: 500;
    font-size: 35px; line-height: 38px; color: var(--forest);
  }
  .headline-rule {
    position: absolute; left: 758px; top: 283px; width: 48px; height: 5px;
    border-radius: 3px; background: var(--forest);
  }

  .loan-terms {
    position: absolute; left: 750px; top: 300px;
    display: grid; grid-template-columns: 101px auto; column-gap: 19px;
    font-size: 14px;
  }
  .loan-terms dt { text-align: right; color: var(--forest); font-weight: 500; line-height: 30px; white-space: nowrap; }
  .loan-terms dd { color: var(--ink); line-height: 30px; white-space: nowrap; }

  .contact {
    position: absolute; left: 744px; top: 576px; width: 305px; height: 188px;
    background: var(--forest); color: var(--paper);
    padding: 18px 0 0 26px;
  }
  .contact-call { font-size: 22px; line-height: 1; }
  .contact-phone { font-size: 45px; font-weight: 500; line-height: 1; margin-top: 6px; }
  .contact-line { display: flex; align-items: center; gap: 10px; font-size: 15px; line-height: 20px; margin-top: 11px; }
  .contact-line.email { margin-top: 17px; }
  .contact-line svg { width: 16px; height: 16px; flex: none; }
</style>
</head>
<body>
  <main class="brochure">
    <div class="city-photo" role="img" aria-label="Black and white aerial view of an Australian city centre skyline with high-rise towers under a cloudy sky"></div>

    <header class="title-block">
      <p class="title-kicker">NEW OFFERING FROM</p>
      <h1 class="title-name">Ferngate<br>Lending</h1>
    </header>

    <div class="brand">
      <span class="brand-dot"></span>
      <span class="brand-name">Ferngate Lending</span>
    </div>

    <h2 class="headline">We did.<br>Just last week.</h2>
    <div class="headline-rule"></div>

    <dl class="loan-terms">
      <dt>Loan Amount:</dt><dd>$854.000</dd>
      <dt>Rate:</dt><dd>8.63%</dd>
      <dt>Term”</dt><dd>12 months</dd>
      <dt>LVR:</dt><dd>56%</dd>
      <dt>Repayments:</dt><dd>Capitalised</dd>
      <dt>Turnaround:</dt><dd>Settled in 7 days</dd>
      <dt>Security:</dt><dd>Lorem ipsum dolor</dd>
      <dt>Purpose:</dt><dd>Ut enim ad minim veniam</dd>
    </dl>

    <section class="contact">
      <p class="contact-call">CALL US TODAY</p>
      <p class="contact-phone">0123456789</p>
      <p class="contact-line email">
        <svg viewBox="0 0 20 20" fill="none" stroke="#fff" stroke-width="1.4"><rect x="1.5" y="4" width="17" height="12"/><path d="M1.5 4l8.5 7 8.5-7M1.5 16l6-5.5M18.5 16l-6-5.5"/></svg>
        info@companyname.com
      </p>
      <p class="contact-line web">
        <svg viewBox="0 0 20 20" fill="none" stroke="#fff" stroke-width="1.4"><circle cx="10" cy="10" r="8.5"/><ellipse cx="10" cy="10" rx="3.8" ry="8.5"/><path d="M1.5 10h17M3 5.5h14M3 14.5h14"/></svg>
        www.companyname.com
      </p>
    </section>
  </main>
</body>
</html>
```